BrindleFlow Van Wrap Design

We are home heating specialists. We fit boilers and central heating systems as well as servicing and repairing boilers in domestic properties. We have a new logo and need our vans design to undergo some modernisation. Our vans are Short wheel base carrow plus.
Website www.BrindleFlow.co.uk
Phone 01632 958274
List of work we do:
Central heating
Installation,
Servicing,
Repairs,
Target Market(s)
Home owners and landlords
Industry/Entity Type
Gas, central heating
Font styles to use
Other font styles liked:
- See logo fonts
Colors
0054AA
0677BA
7BADD7
CADEEF
E8F1F8
EE7325
F08F49
F5BC92
FAE3D3
FDF4ED
Requirements
Must have
- Phone number, logo, web address, Chatterly logo, fuel sound logo, Halden Kruse logo, list of work we do
Nice to have
- Warm design as we are heating specialists.
Should not have
- Too much blue. Our main colour is orange.

```html
<!DOCTYPE html>
<html lang="en">
<head>
<meta charset="utf-8">
<title>BrindleFlow Van Wrap</title>
<link rel="stylesheet" href="https://fonts.googleapis.com/css2?family=Poppins:wght@400;500;600&family=Montserrat:wght@600&display=swap">
<style>
:root{
  --blue:#0054AA;
  --blue-mid:#0677BA;
  --orange:#EE7325;
  --orange-soft:#F08F49;
  --gold:#E8A21E;
  --white:#ffffff;
  --bg:#ffffff;
  --panel-edge:#d9dde3;
}
*{margin:0;padding:0;box-sizing:border-box}
html,body{width:1200px;height:1200px;overflow:hidden;background:var(--bg)}
body{position:relative;font-family:"Poppins",sans-serif;color:var(--blue)}
.panel{position:absolute;overflow:hidden;background:var(--white);border:2px solid var(--panel-edge);border-radius:22px}
.panel svg.bands{position:absolute;inset:0;width:100%;height:100%}
.abs{position:absolute}

.brand{display:flex;flex-direction:column;align-items:center}
.brand-row{display:flex;align-items:center;gap:12px}
.brand-dot{border-radius:50%;background:var(--orange);flex:none}
.brand-name{font-family:"Poppins",sans-serif;font-weight:600;color:var(--orange);line-height:1;white-space:nowrap}
.tagline{font-family:"Montserrat",sans-serif;font-weight:600;color:var(--blue);letter-spacing:.14em;text-transform:uppercase;white-space:nowrap}

.phone{font-weight:500;letter-spacing:.04em;line-height:1;white-space:nowrap}
.web,.email{white-space:nowrap}
.web b{font-weight:600}
.services{display:flex;align-items:stretch;gap:10px}
.services-main{font-weight:400;line-height:1.3}
.services-sub{border-left:2px solid var(--orange);padding-left:8px;line-height:1.25;font-weight:400}
.badges{display:flex;gap:10px;align-items:center}
.badge-cert{background:var(--gold);border-radius:3px;flex:none}
.social{display:flex;align-items:center;gap:6px;font-weight:500;white-space:nowrap}
.social-square{background:var(--blue);border-radius:3px;flex:none}

/* side */
.side{left:50px;top:70px;width:1100px;height:520px}
.side .brand{left:440px;top:60px}
.side .brand-dot{width:64px;height:64px}
.side .brand-name{font-size:52px}
.side .tagline{font-size:13px;margin-top:8px}
.side .contact{left:260px;top:255px}
.side .phone{font-size:30px;color:var(--blue)}
.side .web{font-size:17px;color:var(--orange);margin-top:8px}
.side .email{font-size:17px;color:var(--blue)}
.side .badges{left:110px;top:268px}
.side .badge-cert,.side .social-square{width:24px;height:24px}
.side .social{font-size:11px;color:var(--blue)}
.side .services{left:540px;top:255px}
.side .services-main{font-size:22px;color:var(--blue)}
.side .services-sub{font-size:12px;color:var(--blue)}
.flame-art{position:absolute;left:820px;top:30px;width:230px;height:360px;border-radius:50% 50% 46% 46% / 60% 60% 40% 40%;background:radial-gradient(ellipse at 50% 75%,var(--orange) 0%,var(--orange-soft) 45%,var(--gold) 100%)}

/* front */
.front{left:55px;top:650px;width:530px;height:470px}
.front .brand{left:0;right:0;top:170px}
.front .brand-row{gap:8px}
.front .brand-dot{width:26px;height:26px}
.front .brand-name{font-size:28px}
.front .tagline{font-size:8px;margin-top:4px}

/* rear */
.rear{left:610px;top:650px;width:530px;height:470px}
.rear .brand{left:0;right:0;top:40px}
.rear .brand-dot{width:50px;height:50px}
.rear .brand-name{font-size:42px}
.rear .tagline{font-size:11px;margin-top:6px}
.rear .phone{left:0;right:0;top:180px;text-align:center;font-size:30px;color:var(--white);letter-spacing:.14em}
.rear .badges{left:90px;top:258px}
.rear .badge-cert,.rear .social-square{width:26px;height:26px}
.rear .social-square{background:var(--white)}
.rear .social{font-size:11px;color:var(--white)}
.rear .contact{right:50px;top:252px;text-align:right}
.rear .web{font-size:14px;color:var(--white)}
.rear .email{font-size:14px;color:var(--orange-soft)}
.rear .services{left:265px;top:340px}
.rear .services-main{font-size:17px;color:var(--white)}
.rear .services-sub{font-size:10px;color:var(--white)}
</style>
</head>
<body>

<section class="panel side" aria-label="Side panel">
  <svg class="bands" viewBox="0 0 1100 520" preserveAspectRatio="none" aria-hidden="true">
    <path d="M0 430 H800 Q900 420 1100 300 V470 H0 Z" fill="var(--blue)"/>
    <path d="M780 0 H1100 V310 Q1000 360 930 380 Q1010 250 940 120 Q880 40 780 0 Z" fill="var(--blue)"/>
    <rect x="0" y="470" width="1100" height="8" fill="var(--white)"/>
    <rect x="0" y="478" width="1100" height="42" fill="var(--orange)"/>
  </svg>
  <div class="flame-art" role="img" aria-label="Large orange flame graphic"></div>

  <div class="abs brand">
    <div class="brand-row"><span class="brand-dot"></span><span class="brand-name">BrindleFlow</span></div>
    <div class="tagline">Your home heating specialists</div>
  </div>

  <div class="abs badges">
    <span class="badge-cert" role="img" aria-label="Fuel sound registration badge"></span>
    <span class="social"><span class="social-square"></span>Chatterly</span>
  </div>

  <div class="abs contact">
    <div class="phone">01632 958274</div>
    <div class="web">www.<b>brindleflow</b>.co.uk</div>
    <div class="email">info@brindleflow.co.uk</div>
  </div>

  <div class="abs services">
    <div class="services-main">Installation<br>Servicing<br>Repairs</div>
    <div class="services-sub">Fires<br>Boilers<br>Cookers<br>Plumbing<br>Radiators</div>
  </div>
</section>

<section class="panel front" aria-label="Front panel">
  <svg class="bands" viewBox="0 0 530 470" preserveAspectRatio="none" aria-hidden="true">
    <polygon points="92,130 112,130 150,240 132,240" fill="var(--orange)"/>
    <polygon points="438,130 418,130 380,240 398,240" fill="var(--orange)"/>
  </svg>
  <div class="abs brand">
    <div class="brand-row"><span class="brand-dot"></span><span class="brand-name">BrindleFlow</span></div>
    <div class="tagline">Your home heating specialists</div>
  </div>
</section>

<section class="panel rear" aria-label="Rear panel">
  <svg class="bands" viewBox="0 0 530 470" preserveAspectRatio="none" aria-hidden="true">
    <rect x="0" y="160" width="530" height="20" fill="var(--orange-soft)"/>
    <rect x="0" y="172" width="530" height="58" fill="var(--orange)"/>
    <rect x="0" y="230" width="530" height="240" fill="var(--blue)"/>
  </svg>
  <div class="abs brand">
    <div class="brand-row"><span class="brand-dot"></span><span class="brand-name">BrindleFlow</span></div>
    <div class="tagline">Your home heating specialists</div>
  </div>
  <div class="abs phone">01632 958274</div>
  <div class="abs badges">
    <span class="badge-cert" role="img" aria-label="Fuel sound registration badge"></span>
    <span class="social"><span class="social-square"></span>Chatterly</span>
  </div>
  <div class="abs contact">
    <div class="web">www.<b>brindleflow</b>.co.uk</div>
    <div class="email">info@brindleflow.co.uk</div>
  </div>
  <div class="abs services">
    <div class="services-main">Installation<br>Servicing<br>Repairs</div>
    <div class="services-sub">Fires<br>Boilers<br>Cookers<br>Plumbing<br>Radiators</div>
  </div>
</section>

</body>
</html>
```